Birchvale Lending Business Cards

please see business card design and compass logo design. please make the blue a bit lighter

Contact Information for Business Card

Marnie Holt
Proprietor
Dip Finance & Mortgage Broking Management (this can be shortened)
LBCN
ACR *****
ABN ****
Mobile
Email

Logo Text

home, business, asset finance

Colors
ffcf3e
ffc214
33a6d7
85acd3
3277b5
ffffff

Requirements
Should not have
• pictures of oceans or cities. I am not trying to replicate a fishing company

```html
<!DOCTYPE html>
<html lang="en">
<head>
<meta charset="utf-8">
<title>Birchvale Lending — Business Cards</title>
<link rel="stylesheet" href="https://fonts.googleapis.com/css2?family=Montserrat:wght@700&family=Arimo:wght@400&display=swap">
<style>
  :root {
    --brand-blue: #3277b5;
    --brand-sky: #33a6d7;
    --accent-gold: #ffc214;
    --paper: #ffffff;
    --ink: #3a3a3a;
    --backdrop: #e9e6e1;
  }
  html, body {
    margin: 0;
    padding: 0;
    width: 1200px;
    height: 900px;
    overflow: hidden;
    background: var(--backdrop);
  }
  .sheet {
    position: relative;
    width: 1200px;
    height: 900px;
  }
  .card {
    position: absolute;
    left: 250px;
    width: 700px;
    height: 400px;
    overflow: hidden;
    box-shadow: 0 6px 18px rgba(0,0,0,0.18);
  }
  .card--back {
    top: 40px;
    background: var(--brand-blue);
    display: flex;
    align-items: center;
    justify-content: center;
  }
  .card--front {
    top: 470px;
    background: var(--paper);
  }
  .wordmark {
    display: flex;
    align-items: center;
    gap: 18px;
    font-family: "Montserrat", sans-serif;
    font-weight: 700;
    text-transform: uppercase;
    line-height: 0.95;
    letter-spacing: 0.5px;
  }
  .wordmark__square {
    flex: none;
    border-style: solid;
    box-sizing: border-box;
  }
  .card--back .wordmark { color: var(--paper); font-size: 58px; }
  .card--back .wordmark__square { width: 110px; height: 110px; border-width: 14px; border-color: var(--paper); }
  .card--front .wordmark {
    position: absolute;
    top: 48px;
    right: 40px;
    color: var(--brand-blue);
    font-size: 32px;
    gap: 12px;
  }
  .card--front .wordmark__square { width: 62px; height: 62px; border-width: 8px; border-color: var(--brand-blue); }
  .holder {
    position: absolute;
    top: 70px;
    left: 48px;
    font-family: "Arimo", sans-serif;
    color: var(--ink);
    font-size: 17px;
    line-height: 1.3;
  }
  .holder__name {
    margin: 0 0 4px;
    font-family: "Montserrat", sans-serif;
    font-weight: 700;
    font-size: 27px;
    color: var(--brand-blue);
    text-transform: uppercase;
    letter-spacing: 0.5px;
  }
  .holder__role, .holder__qual { margin: 0; }
  .swoosh {
    position: absolute;
    inset: 0;
    width: 700px;
    height: 400px;
  }
  .contact {
    position: absolute;
    left: 90px;
    top: 205px;
    margin: 0;
    padding: 0;
    list-style: none;
    font-family: "Arimo", sans-serif;
    font-size: 18px;
    color: var(--ink);
  }
  .contact__item { display: flex; align-items: center; gap: 10px; margin-bottom: 6px; }
  .contact__icon { width: 18px; height: 18px; flex: none; }
  .credentials {
    position: absolute;
    right: 38px;
    top: 225px;
    margin: 0;
    text-align: right;
    font-family: "Arimo", sans-serif;
    font-size: 15px;
    line-height: 1.35;
    color: var(--paper);
  }
</style>
</head>
<body>
<main class="sheet">

  <section class="card card--back" aria-label="Business card, back">
    <div class="wordmark">
      <span class="wordmark__square" aria-hidden="true"></span>
      <span>Birchvale<br>Lending</span>
    </div>
  </section>

  <section class="card card--front" aria-label="Business card, front">
    <svg class="swoosh" viewBox="0 0 700 400" aria-hidden="true">
      <path fill="var(--accent-gold)" d="M0,338 C180,340 350,305 480,228 C395,302 205,356 0,360 Z"/>
      <path fill="var(--brand-blue)" d="M0,366 C200,364 390,320 530,245 C610,203 655,178 700,168 L700,400 L0,400 Z"/>
    </svg>

    <div class="holder">
      <h1 class="holder__name">Marnie Holt</h1>
      <p class="holder__role">Proprietor</p>
      <p class="holder__qual">Dip Finance &amp; Mortgage<br>Broking Management</p>
    </div>

    <div class="wordmark">
      <span class="wordmark__square" aria-hidden="true"></span>
      <span>Birchvale<br>Lending</span>
    </div>

    <ul class="contact">
      <li class="contact__item">
        <svg class="contact__icon" viewBox="0 0 18 18" aria-hidden="true">
          <rect x="4" y="1.5" width="10" height="15" rx="2" fill="none" stroke="var(--brand-blue)" stroke-width="2"/>
          <circle cx="9" cy="13.5" r="1" fill="var(--brand-blue)"/>
        </svg>
        <span>044-987 654 321</span>
      </li>
      <li class="contact__item">
        <svg class="contact__icon" viewBox="0 0 18 18" aria-hidden="true">
          <rect x="1" y="4" width="16" height="11" fill="var(--brand-blue)"/>
          <path d="M1,4 L9,10 L17,4" fill="none" stroke="var(--paper)" stroke-width="1.5"/>
        </svg>
        <span>hello@birchvale.com</span>
      </li>
    </ul>

    <p class="credentials">LBCN<br>ACR 472913<br>ABN 38104627</p>
  </section>

</main>
</body>
</html>
```